依頼詳細
制作目的
講座の参加者を募集するため。

用途
自然學校HPにPDFを掲載。チラシに掲載したQRコードを読み取り、申込フォームから申し込んでもらう。また、講師など関係者を通じてその所属大学や近隣の大学に配布。

ターゲット
学生(大学生や専門学生、短大生など)20名、若手社会人(20~30代前半)数名
特に、SDGsに興味関心があり、学びや対話に意欲的な方。社会課題に対して意識が高く、自身でも何かアクションを起こしたいと考えている方の参加を期待します。
記載項目
記載原稿については添付ファイルをご確認ください。
使用画像については、下記URLよりダウンロードをお願いいたします。
https://3.kumodrop.jp/0927-8b2c41e7a90d35f6c1b4e07d2a96f3c1

画像について、当自然學校のHP内で掲載している写真を使っていただいても構いません。元データをお送りすることも可能ですのでお申し付けください。また追加で必要な画像等がありましたらご相談ください。

表面:イベントタイトル/キャッチコピー/メイン写真(活動風景写真から選出)/サブ写真(白川郷)/イベント概要と趣旨/日程/参加費/定員/会場/対象/主催者/後援
裏面:イベントタイトル/日程と講座の詳細/滞在イメージ写真/活動風景写真/会場アクセス/申込方法/施設ロゴ
サイズ
A4
ページ数
両面
希望イメージ
シンプル 複雑
単色 カラフル
暗い 明るい
日常 高級
遊び心 厳粛
未来的 伝統的
女性的 男性的
希望する色
設定なし
納品ファイル
• イラストレーター形式 (.ai)
補足説明
イラストレーター形式及び高解像度PDFでも納品をお願いしたいです。ネット印刷を予定しております。
■ 選んだ理由

フォントや配色などやわらかな印象で若者向けのデザインかつ、裏面のすっきりと見やすい構成が良いと思い選定しました。

■ 提案者全員のお礼・コメント

短い期間にもかかわらず、ご提案をいただきましてありがとうございました。シンプルで洗練されたデザインや、メリハリのある裏面の構成、ターゲットの若者を意識したフォントなどそれぞれ素敵なデザインで、選定が悩ましかったです。またの機会がございましたら、ご提案いただければ幸いです。この度は誠にありがとうございました。

```html
<!DOCTYPE html>
<html lang="ja">
<head>
<meta charset="utf-8">
<title>2022年度 SDGs担い手育成講座 参加者募集</title>
<link rel="stylesheet" href="https://fonts.googleapis.com/css2?family=M+PLUS+Rounded+1c:wght@500;700;800&family=Zen+Maru+Gothic:wght@500;700&display=swap">
<style>
  :root {
    --bg: #eef3d6;
    --green: #2f7a3e;
    --green-dark: #245c30;
    --accent: #e8792b;
    --text: #33402c;
    --white: #ffffff;
    --photo-main-a: #7d8a5c;
    --photo-main-b: #b88a4a;
    --photo-sub-a: #6f7e52;
    --photo-sub-b: #a9b38a;
  }
  * { margin: 0; padding: 0; box-sizing: border-box; }
  html, body { width: 859px; height: 1200px; overflow: hidden; }
  body { background: var(--white); font-family: "Zen Maru Gothic", sans-serif; color: var(--text); }
  .flyer { position: relative; width: 859px; height: 1200px; background: var(--bg); overflow: hidden; }

  .header { position: absolute; left: 40px; top: 26px; }
  .header .year { font-family: "M PLUS Rounded 1c", sans-serif; font-weight: 700; font-size: 22px; color: var(--green); letter-spacing: 1px; }
  .header .title { display: flex; align-items: baseline; gap: 12px; margin-top: -4px; }
  .header .sdgs { font-family: "M PLUS Rounded 1c", sans-serif; font-weight: 800; font-size: 78px; color: var(--accent); letter-spacing: -2px; }
  .header .course { font-family: "M PLUS Rounded 1c", sans-serif; font-weight: 800; font-size: 64px; color: var(--green-dark); letter-spacing: 2px; }

  .badge { position: absolute; right: 52px; top: 70px; width: 96px; height: 96px; border-radius: 50%; background: var(--white); border: 3px solid var(--green); display: flex; align-items: center; justify-content: center; text-align: center; font-family: "M PLUS Rounded 1c", sans-serif; font-weight: 800; color: var(--green); font-size: 20px; line-height: 1.2; z-index: 2; }

  .photo { position: absolute; }
  .photo-main { left: 0; top: 160px; width: 859px; height: 420px; background: linear-gradient(160deg, var(--photo-main-a), var(--photo-main-b) 60%, #5c6b44); clip-path: polygon(0 0, 100% 6%, 100% 78%, 0 100%); }
  .photo-sub { right: 0; top: 440px; width: 420px; height: 190px; background: linear-gradient(150deg, var(--photo-sub-a), var(--photo-sub-b)); clip-path: polygon(8% 12%, 100% 0, 100% 100%, 0 100%); }

  .ribbon { position: absolute; background: var(--white); color: var(--green-dark); font-family: "M PLUS Rounded 1c", sans-serif; font-weight: 800; padding: 6px 22px; }
  .ribbon-top { left: 34px; top: 222px; font-size: 26px; transform: rotate(-3deg); }
  .ribbon-bottom { left: 60px; top: 572px; font-size: 32px; transform: rotate(-5deg); padding: 8px 28px; }

  .lead { position: absolute; left: 0; right: 0; top: 664px; text-align: center; font-size: 18px; font-weight: 700; line-height: 1.7; letter-spacing: 0.5px; }

  .info { position: absolute; left: 40px; right: 40px; top: 852px; display: grid; grid-template-columns: 1fr 1fr; column-gap: 28px; row-gap: 26px; }
  .info-item { display: flex; gap: 14px; align-items: flex-start; }
  .info-label { flex: none; width: 68px; padding: 6px 0; background: var(--green); color: var(--white); font-weight: 700; font-size: 17px; text-align: center; border-radius: 4px; }
  .info-body { flex: 1; font-size: 17px; font-weight: 700; line-height: 1.45; }
  .info-body small { display: block; font-size: 12px; font-weight: 500; }
  .info-body .fee { font-family: "M PLUS Rounded 1c", sans-serif; font-size: 30px; font-weight: 800; color: var(--green-dark); }
  .target-row { display: flex; justify-content: space-between; gap: 12px; }

  .footer { position: absolute; left: 0; right: 0; bottom: 0; height: 54px; background: var(--green); color: var(--white); display: flex; align-items: center; justify-content: center; gap: 28px; font-size: 15px; font-weight: 700; }
</style>
</head>
<body>
<main class="flyer">
  <header class="header">
    <p class="year">2022年度</p>
    <h1 class="title"><span class="sdgs">SDGs</span><span class="course">担い手育成講座</span></h1>
  </header>

  <div class="badge">参加者<br>募集</div>

  <div class="photo photo-main" role="img" aria-label="ヘルメットを被った参加者たちが紅葉の山中で並ぶ集合写真"></div>
  <div class="photo photo-sub" role="img" aria-label="合掌造り集落の風景写真"></div>

  <p class="ribbon ribbon-top">白川郷から未来へ</p>
  <p class="ribbon ribbon-bottom">学生が本気で考える10年後</p>

  <p class="lead">
    長い期間人々に受け継がれてきた文化や建物が残る白川郷って、<br>
    意外と「サステイナブルな未来」の最前線なのかも。<br>
    そんな地の文化に触れ、そこに住む人や最先端で活躍する人から話を聞き、<br>
    共に過ごす仲間や子どもたちと語り、<br>
    さあ、あなたのそして社会の未来のために何をしようか。
  </p>

  <section class="info">
    <div class="info-item">
      <span class="info-label">期間</span>
      <div class="info-body">2022年7月〜2023年2月<small>（土曜日・各2泊3日）開催日程は裏面参照</small></div>
    </div>
    <div class="info-item">
      <span class="info-label">対象</span>
      <div class="info-body">
        <div class="target-row"><span>学生<small>（大学生、専門学生、短大生など）</small></span><span>20名</span></div>
        <div class="target-row"><span>若手社会人<small>（20〜30代前半）</small></span><span>数名</span></div>
      </div>
    </div>
    <div class="info-item">
      <span class="info-label">会場</span>
      <div class="info-body">白川郷もりの自然学校<small>（みどり県もりの里村）</small></div>
    </div>
    <div class="info-item">
      <span class="info-label">参加費</span>
      <div class="info-body">各回<span class="fee">8,000</span>円<small>（2泊6食を含む）※交通費は別途自己負担</small></div>
    </div>
  </section>

  <footer class="footer">
    <span>主催：ミドリ自動車株式会社／白川郷もりの自然学校</span>
    <span>後援：もりの里村</span>
  </footer>
</main>
</body>
</html>
```